Business Card Design

We are a commercial real estate brokerage in San Francisco, leasing office buildings downtown.
I would like a clean, elegant look. Simple but powerful .

Industry/Entity Type

Business

Contact Information for Business Card

Colin Farrow
lic# 07281549
415.555.0172
colin@tarvo-commercial.example
tarvo-commercial.example

```html
<!DOCTYPE html>
<html lang="en">
<head>
<meta charset="utf-8">
<title>Tarvo Commercial – Business Card</title>
<link rel="stylesheet" href="https://fonts.googleapis.com/css2?family=Open+Sans:wght@300;400;600;700&display=swap">
<style>
  :root {
    --backdrop: #e9e9e7;
    --card-white: #ffffff;
    --slate: #6b7d99;
    --slate-light: #c9d0dc;
    --ink: #3a3a3a;
    --rule: #2b2b2b;
    --mark: #8a8f96;
    --on-slate: #ffffff;
  }
  * { margin: 0; padding: 0; box-sizing: border-box; }
  html, body {
    width: 1200px; height: 806px; overflow: hidden;
    background: var(--backdrop);
    font-family: "Open Sans", Arial, sans-serif;
  }
  .card {
    position: absolute; left: 50px; top: 80px;
    width: 1100px; height: 647px;
    background: var(--card-white);
    overflow: hidden;
  }
  .card__band {
    position: absolute; left: 0; top: 292px; width: 100%; height: 355px;
    background: linear-gradient(90deg, var(--slate) 0%, var(--slate) 72%, var(--slate-light) 100%);
  }
  .card__notch { position: absolute; left: 452px; top: 291px; }
  .card__divider {
    position: absolute; left: 476px; top: 49px;
    width: 4px; height: 481px; background: var(--rule);
  }
  .brand-mark {
    position: absolute; left: 314px; top: 73px;
    width: 140px; height: 140px; background: var(--mark);
  }
  .brand-name {
    position: absolute; left: 503px; top: 52px;
    color: var(--slate); font-weight: 700; line-height: 1;
  }
  .brand-name__main { display: block; font-size: 124px; letter-spacing: 1px; }
  .brand-name__sub { display: block; font-size: 48px; letter-spacing: 1px; margin-top: 4px; }
  .website {
    position: absolute; left: 507px; top: 228px;
    font-size: 30px; font-weight: 600; color: var(--ink);
  }
  .person {
    position: absolute; right: 654px; top: 415px;
    text-align: right; color: var(--on-slate);
  }
  .person__name { font-size: 36px; font-weight: 600; line-height: 1.2; }
  .person__licence { font-size: 30px; font-weight: 300; margin-top: 6px; }
  .contact {
    position: absolute; left: 507px; top: 420px;
    list-style: none; color: var(--on-slate);
    font-size: 28px; font-weight: 700;
  }
  .contact__item { display: flex; align-items: center; height: 42px; }
  .contact__icon { width: 30px; margin-right: 14px; flex: none; }
</style>
</head>
<body>
  <div class="card">
    <div class="card__band"></div>
    <svg class="card__notch" width="54" height="28" viewBox="0 0 54 28">
      <polygon points="0,0 54,0 27,28" fill="#ffffff"/>
    </svg>
    <div class="card__divider"></div>

    <div class="brand-mark"></div>
    <div class="brand-name">
      <span class="brand-name__main">TARVO</span>
      <span class="brand-name__sub">COMMERCIAL</span>
    </div>
    <div class="website">tarvo-commercial.example</div>

    <div class="person">
      <div class="person__name">Colin Farrow</div>
      <div class="person__licence">Lic Nr. 07281549</div>
    </div>

    <ul class="contact">
      <li class="contact__item">
        <svg class="contact__icon" viewBox="0 0 30 30" aria-hidden="true">
          <rect x="7" y="2" width="16" height="26" rx="3" fill="none" stroke="#fff" stroke-width="2.5"/>
          <line x1="13" y1="23.5" x2="17" y2="23.5" stroke="#fff" stroke-width="2.5"/>
        </svg>
        415.555.0172
      </li>
      <li class="contact__item">
        <svg class="contact__icon" viewBox="0 0 30 30" aria-hidden="true">
          <rect x="2" y="7" width="26" height="17" fill="none" stroke="#fff" stroke-width="2.5"/>
          <polyline points="2,7 15,17 28,7" fill="none" stroke="#fff" stroke-width="2.5"/>
        </svg>
        colin@tarvo-commercial.example
      </li>
    </ul>
  </div>
</body>
</html>
```